Corvane

I'm looking for business cards with the logo I've attached. I don't have an specific idea in mind and open to anything. All the usual info will be involved. Name, position in company, nr, email, address

```html
<!DOCTYPE html>
<html lang="en">
<head>
<meta charset="utf-8">
<title>Corvane Business Cards</title>
<link href="https://fonts.googleapis.com/css2?family=Lato:wght@400;700&display=swap" rel="stylesheet">
<style>
  :root {
    --backdrop: #616161;
    --navy: #1a2f4e;
    --gold: #edb03a;
    --paper: #ffffff;
    --ink: #1b1b1b;
  }
  html, body {
    margin: 0;
    padding: 0;
    width: 1075px;
    height: 1200px;
    overflow: hidden;
    background: var(--backdrop);
    font-family: "Lato", Arial, sans-serif;
  }
  .stage {
    position: absolute;
    left: 0;
    top: 0;
    width: 1196px;
    height: 1335px;
    transform: scale(0.8988);
    transform-origin: 0 0;
  }
  .card {
    position: absolute;
    left: 229px;
    width: 738px;
    height: 440px;
    box-shadow: 3px 3px 3px rgba(0,0,0,0.55);
    overflow: hidden;
  }
  .card--front { top: 208px; background: var(--paper); }
  .card--back { top: 709px; background: var(--navy); }

  .wave { position: absolute; inset: 0; width: 738px; height: 440px; }

  .brand {
    position: absolute;
    display: flex;
    flex-direction: column;
    align-items: center;
  }
  .brand__dot { border-radius: 50%; }
  .brand__name {
    color: var(--gold);
    font-weight: 700;
    letter-spacing: 1px;
    line-height: 1;
    text-transform: uppercase;
  }
  .card--front .brand { left: 46px; top: 52px; width: 256px; }
  .card--front .brand__dot { width: 62px; height: 62px; background: var(--navy); margin-bottom: 34px; }
  .card--front .brand__name { font-size: 52px; }
  .card--back .brand { left: 0; top: 100px; width: 738px; }
  .card--back .brand__dot { width: 84px; height: 84px; background: var(--paper); margin-bottom: 50px; }
  .card--back .brand__name { font-size: 68px; }

  .person {
    position: absolute;
    right: 55px;
    top: 56px;
    text-align: right;
  }
  .person__name {
    color: var(--gold);
    font-size: 28px;
    font-weight: 700;
    line-height: 1.05;
    text-transform: uppercase;
  }
  .person__role {
    color: var(--ink);
    font-size: 20px;
    margin-right: 5px;
  }

  .contact {
    position: absolute;
    right: 54px;
    top: 268px;
    margin: 0;
    padding: 0;
    list-style: none;
    color: var(--paper);
    font-size: 20px;
    text-align: right;
  }
  .contact__item {
    display: flex;
    justify-content: flex-end;
    align-items: center;
    gap: 8px;
    height: 27.5px;
  }
  .contact__item--address {
    margin-top: 15px;
    height: auto;
    align-items: flex-start;
    line-height: 26px;
  }
  .contact__icon { width: 20px; height: 20px; flex: none; fill: var(--gold); }
  .contact__item--address .contact__icon { margin-top: 4px; }
</style>
</head>
<body>
<div class="stage">

  <section class="card card--front">
    <svg class="wave" viewBox="0 0 738 440" aria-hidden="true">
      <path d="M0,277 C130,330 250,300 345,240 C250,310 120,335 0,312 Z" fill="var(--gold)"/>
      <path d="M0,318 C130,350 270,330 390,265 C480,215 560,175 645,168 C690,170 720,190 738,205 V440 H0 Z" fill="var(--navy)"/>
      <path d="M600,178 C620,170 635,168 646,168 C630,168 612,172 600,178 Z" fill="var(--navy)"/>
      <path d="M88,367 C210,392 320,350 440,275 C520,225 580,185 645,168 C575,174 505,200 420,255 C310,325 200,378 88,367 Z" fill="var(--paper)"/>
    </svg>

    <div class="brand">
      <span class="brand__dot"></span>
      <span class="brand__name">Corvane</span>
    </div>

    <div class="person">
      <div class="person__name">Marcus Hale</div>
      <div class="person__role">Managing Director</div>
    </div>

    <ul class="contact">
      <li class="contact__item">041-275 830 614
        <svg class="contact__icon" viewBox="0 0 24 24"><path d="M6.6 10.8a15.1 15.1 0 0 0 6.6 6.6l2.2-2.2a1 1 0 0 1 1-.25 11.4 11.4 0 0 0 3.6.57 1 1 0 0 1 1 1V20a1 1 0 0 1-1 1A17 17 0 0 1 3 4a1 1 0 0 1 1-1h3.5a1 1 0 0 1 1 1c0 1.25.2 2.45.57 3.6a1 1 0 0 1-.25 1z"/></svg>
      </li>
      <li class="contact__item">hello@corvanemail.com
        <svg class="contact__icon" viewBox="0 0 24 24"><path d="M2 5h20v14H2z M3.5 6.5 12 13l8.5-6.5" fill="var(--gold)" stroke="var(--navy)" stroke-width="1.4"/></svg>
      </li>
      <li class="contact__item">www.corvanestudio.com
        <svg class="contact__icon" viewBox="0 0 24 24"><circle cx="12" cy="12" r="10"/><path d="M2 12h20M12 2v20M4.5 7h15M4.5 17h15M12 2c-4 4-4 16 0 20M12 2c4 4 4 16 0 20" fill="none" stroke="var(--navy)" stroke-width="1.3"/></svg>
      </li>
      <li class="contact__item contact__item--address">
        <span>87 Harbour Lane<br>Westmere, 30917</span>
        <svg class="contact__icon" viewBox="0 0 24 24"><path d="M12 2a7 7 0 0 0-7 7c0 5 7 13 7 13s7-8 7-13a7 7 0 0 0-7-7zm0 9.5A2.5 2.5 0 1 1 12 6.5a2.5 2.5 0 0 1 0 5z"/></svg>
      </li>
    </ul>
  </section>

  <section class="card card--back">
    <div class="brand">
      <span class="brand__dot"></span>
      <span class="brand__name">Corvane</span>
    </div>
  </section>

</div>
</body>
</html>
```